PROPERTY DEVELOPERS - LOGO & STATIONERY

We require a new logo design for a property development and sales company in Sydney, Australia.

We source land, build and sell residential & commercial investment properties including apartment buildings, townhouses, house and land packages in estates and retail shops.

We sell to local and overseas markets therefore the design needs to be a corporate effective global logo that would also suit the Asian market.

The company name is Corvane and we have been operating for 11 years and have been involved with over 5,000 properties. The focus should be on our company name Corvane with the word property as the word to explain ourselves.

This brief includes the logo design, business cards, letterhead, envelopes, with compliments slips and address label stickers.

We look forward to receiving exciting new designs.
All the best.

Reason: Designer who we were going to choose had their account closed.  Need some more options!

Property

Corvane Property

```html
<!DOCTYPE html>
<html lang="en">
<head>
<meta charset="utf-8">
<title>Corvane Property – Business Card</title>
<link rel="stylesheet" href="https://fonts.googleapis.com/css2?family=Mulish:wght@400&display=swap">
<style>
  :root {
    --paper: #ffffff;
    --ink: #111111;
    --muted: #9a9a9a;
    --rule: #b5b5b5;
    --mark: #8f8f8f;
  }
  html, body {
    margin: 0;
    padding: 0;
    overflow: hidden;
    background: var(--paper);
  }
  .card {
    position: relative;
    width: 1200px;
    height: 733px;
    background: var(--paper);
    font-family: "Mulish", sans-serif;
    overflow: hidden;
  }
  .brand {
    position: absolute;
    left: 0;
    right: 0;
    top: 160px;
    display: flex;
    justify-content: center;
    align-items: center;
    gap: 18px;
    color: var(--mark);
    font-size: 40px;
    font-weight: 400;
    letter-spacing: 0.08em;
    text-transform: uppercase;
  }
  .brand__square {
    width: 22px;
    height: 22px;
    background: var(--mark);
  }
  .holder-name {
    position: absolute;
    left: 0;
    right: 0;
    top: 385px;
    margin: 0;
    text-align: center;
    color: var(--ink);
    font-size: 40px;
    font-weight: 400;
    letter-spacing: 0.02em;
    text-transform: uppercase;
  }
  .divider {
    position: absolute;
    left: 48px;
    top: 502px;
    width: 1107px;
    height: 1px;
    background: var(--rule);
  }
  .contact {
    position: absolute;
    left: 0;
    right: 0;
    top: 531px;
    margin: 0;
    text-align: center;
    color: var(--muted);
    font-size: 33px;
    line-height: 43px;
    font-style: normal;
    text-transform: uppercase;
  }
  .contact__line {
    display: block;
    white-space: nowrap;
  }
  .contact__gap {
    display: inline-block;
    width: 30px;
  }
</style>
</head>
<body>
  <div class="card">
    <div class="brand">
      <span class="brand__square"></span>
      <span class="brand__name">Corvane Property</span>
    </div>

    <h1 class="holder-name">Helena Marisotis</h1>

    <div class="divider"></div>

    <address class="contact">
      <span class="contact__line">Level 14, Tower One Harbourside, 58 Calder Street</span>
      <span class="contact__line">Eastbrook Junction, New South Wales 2031</span>
      <span class="contact__line">M: (+61) 0400 555 317<span class="contact__gap"></span>T: 1300 555 864</span>
      <span class="contact__line">E: helena@corvaneproperty.com.au</span>
    </address>
  </div>
</body>
</html>
```